nestliva - Ballon Design

I need a Ballon designed. Please use the psb file ballon_template.psb as template.

I would like to have a ballon designed similar to the file "example.png".
instead of the pellu tot logo please use my attached logo "nestliva logo.ai"

The text should be the same " IT'S A MOM" but the logo should be different.

I should look like more elegant. should be also white background. But for the design feel free.

thanks.

Please also add the webpage "www.nestliva.eu" on the ballon design.

```html
<!DOCTYPE html>
<html lang="en">
<head>
<meta charset="utf-8">
<title>nestliva – It's a Mom balloon</title>
<link rel="stylesheet" href="https://fonts.googleapis.com/css2?family=Poppins:wght@700;800;900&display=swap">
<style>
  :root {
    --backdrop: #d1d2d4;
    --balloon: #ffffff;
    --rose: #d0809f;
    --navy: #3f64a0;
  }
  html, body {
    margin: 0;
    padding: 0;
    width: 1019px;
    height: 1200px;
    overflow: hidden;
    background: var(--backdrop);
  }
  .canvas {
    position: relative;
    width: 1019px;
    height: 1200px;
    background: var(--backdrop);
    font-family: "Poppins", Arial, sans-serif;
  }
  .balloon-shape {
    position: absolute;
    inset: 0;
  }
  .headline {
    position: absolute;
    left: 0;
    width: 1019px;
    top: 190px;
    margin: 0;
    text-align: center;
    color: var(--rose);
    font-weight: 900;
    font-size: 186px;
    line-height: 142px;
    letter-spacing: -2px;
    text-transform: uppercase;
  }
  .headline span { display: block; }
  .brand-name {
    position: absolute;
    left: 0;
    width: 1019px;
    top: 650px;
    margin: 0;
    text-align: center;
    color: var(--navy);
    font-weight: 700;
    font-size: 84px;
    line-height: 100px;
    letter-spacing: 1px;
  }
  .web-address {
    position: absolute;
    left: 0;
    width: 1019px;
    top: 764px;
    margin: 0;
    text-align: center;
    color: var(--navy);
    font-weight: 700;
    font-size: 27px;
    line-height: 36px;
  }
</style>
</head>
<body>
  <main class="canvas">
    <svg class="balloon-shape" width="1019" height="1200" viewBox="0 0 1019 1200" aria-hidden="true">
      <circle cx="509" cy="491" r="396" fill="var(--balloon)"/>
      <path d="M468 872 C462 930 448 985 452 1030 C455 1060 470 1070 478 1080 C482 1092 486 1104 509 1106 C532 1104 536 1092 540 1080 C548 1070 563 1060 566 1030 C570 985 556 930 550 872 Z" fill="var(--balloon)"/>
      <circle cx="509" cy="1090" r="4" fill="var(--backdrop)"/>
    </svg>

    <h1 class="headline">
      <span>It’s</span>
      <span>A</span>
      <span>Mom</span>
    </h1>

    <p class="brand-name">nestliva</p>
    <p class="web-address">www.nestliva.eu</p>
  </main>
</body>
</html>
```